Home Renovation Business needs a logo and business card design

I need a logo design for my home renovation company. I work hard to provide quality work for a fair price. I want a clean design that has something to make it pop and catch the eye. It should have somewhat of a modern feel to it. You can check out my website at www.kbbuildworks.com to see some examples of the type of work I do.
Updates

Hi Everyone,

For some reason, not all my information was posted. I would like the following contact information included in the design:

Phone: 365.417.9826        Email: kdrosmol@maplepost.ca        Website: www.kbbuildworks.com

Also, if you would like to include a list of the services I offer, then I'd like the card to be double sided. I provide the following services: Full kitchen, basement and bathroom renovations. Tile, laminate and hardwood installation. Decks, fences and sheds. Windows and doors.

Industry/Entity Type

Business

Requirements
Must have
• I want the following information listed on the card:
• KD Buildworks
• Kyle Drosmolen
• 365.417.9826
• kdrosmol@maplepost.ca
• www.kbbuildworks.com
Nice to have
• If you want you could also include the list of services I provide. If you include this list feel free to make the card double sided.
• Kitchen, bathroom and basement renovations
• Flooring installation
• Decks, fences and sheds
• Windows and doors
• I am not 100% sure if I want to include this on the card or not.

```html
<!DOCTYPE html>
<html lang="en">
<head>
<meta charset="utf-8">
<title>KD Buildworks – Business Card Colourways</title>
<link rel="stylesheet" href="https://fonts.googleapis.com/css2?family=Arimo:wght@400;700&family=Open+Sans:wght@700&family=Tinos&display=swap">
<style>
  :root {
    --page: #ffffff;
    --card: #ffffff;
    --card-soft: #f2f2f2;
    --ink: #1d1d1d;
    --white: #ffffff;
    --blue: #1e6cc0;
    --blue-light: #4a8fd6;
    --red: #ff2a2a;
    --red-light: #ff5a5a;
    --orange: #ff7410;
    --orange-light: #ff9640;
    --purple: #7414ff;
    --purple-light: #9a52ff;
    --pink: #ff18c8;
    --pink-light: #ff5ad8;
    --slate: #65698f;
    --slate-light: #8a8dab;
  }
  * { margin: 0; padding: 0; box-sizing: border-box; }
  html, body { width: 1200px; height: 900px; overflow: hidden; background: var(--page); }
  .sheet { position: relative; width: 1200px; height: 900px; }

  .card {
    position: absolute;
    width: 507px; height: 262px;
    background: var(--card);
    box-shadow: 2px 3px 4px rgba(0,0,0,.45);
    overflow: hidden;
    color: var(--ink);
  }
  .card--blue   { --accent: var(--blue);   --accent-light: var(--blue-light);   left: 92px;  top: 31px; }
  .card--red    { --accent: var(--red);    --accent-light: var(--red-light);    left: 624px; top: 31px; }
  .card--orange { --accent: var(--orange); --accent-light: var(--orange-light); left: 92px;  top: 320px; }
  .card--purple { --accent: var(--purple); --accent-light: var(--purple-light); left: 624px; top: 320px; }
  .card--pink   { --accent: var(--pink);   --accent-light: var(--pink-light);   left: 92px;  top: 608px; }
  .card--slate  { --accent: var(--slate);  --accent-light: var(--slate-light);  left: 624px; top: 608px; background: var(--card-soft); }

  .card__art { position: absolute; inset: 0; width: 507px; height: 262px; }
  .card__panel { fill: var(--accent); }
  .card__stripe { fill: var(--accent-light); }

  .brand {
    position: absolute; left: 0; top: 72px; width: 196px;
    text-align: center; color: var(--white);
  }
  .brand__dot {
    display: block; width: 40px; height: 40px; margin: 0 auto 12px;
    border-radius: 50%; background: rgba(255,255,255,.85);
  }
  .brand__name {
    font-family: "Open Sans", Arial, sans-serif; font-weight: 700;
    font-size: 15px; letter-spacing: .2px;
  }

  .holder {
    position: absolute; left: 243px; top: 32px;
    display: flex; align-items: baseline; white-space: nowrap;
  }
  .holder__mark { width: 8px; height: 12px; margin-right: 8px; fill: var(--accent); align-self: center; }
  .holder__name {
    font-family: "Tinos", "Times New Roman", serif; font-size: 16px;
    color: var(--accent); letter-spacing: .4px; text-transform: uppercase;
  }
  .holder__role {
    font-family: "Arimo", Arial, sans-serif; font-size: 9px;
    margin-left: 12px;
  }

  .contacts {
    position: absolute; left: 300px; top: 130px; list-style: none;
    font-family: "Arimo", Arial, sans-serif; font-size: 11.5px; line-height: 14px;
  }
  .contacts__item { display: flex; align-items: flex-start; margin-bottom: 18px; }
  .contacts__item:nth-child(3) { margin-bottom: 12px; }
  .contacts__icon { width: 14px; height: 14px; margin-right: 20px; flex: none; fill: var(--accent); color: var(--accent); }
</style>
</head>
<body>
<main class="sheet">

  <!-- Shared card markup repeated per colourway -->
  <section class="card card--blue">
    <svg class="card__art" viewBox="0 0 507 262" aria-hidden="true">
      <polygon class="card__panel" points="0,0 158,0 212,128 140,262 0,262"/>
      <polygon class="card__stripe" points="166,0 184,0 232,128 166,262 148,262 214,128"/>
    </svg>
    <div class="brand"><span class="brand__dot"></span><span class="brand__name">KD BUILDWORKS</span></div>
    <div class="holder">
      <svg class="holder__mark" viewBox="0 0 8 12"><polygon points="0,0 3,0 8,6 3,12 0,12 5,6"/></svg>
      <span class="holder__name">Kyle Drosmolen</span><span class="holder__role">(Managing Director)</span>
    </div>
    <ul class="contacts">
      <li class="contacts__item"><svg class="contacts__icon" viewBox="0 0 14 14"><path d="M3 1l2.2 2.6-1.2 1.6c.8 1.8 2 3 3.8 3.8l1.6-1.2L12 10l-1 2.5C5.8 12.3 1.7 8.2 1.5 3z"/></svg>365-417-9826</li>
      <li class="contacts__item"><svg class="contacts__icon" viewBox="0 0 14 14"><path d="M1 3h12v1.2L7 8 1 4.2z M1 5.6l6 3.8 6-3.8V11H1z"/></svg>info@kbbuildworks.com</li>
      <li class="contacts__item"><svg class="contacts__icon" viewBox="0 0 14 14"><path d="M7 1a4 4 0 0 1 4 4c0 3-4 8-4 8S3 8 3 5a4 4 0 0 1 4-4zm0 2.4A1.6 1.6 0 1 0 7 6.6 1.6 1.6 0 0 0 7 3.4z"/></svg><span>14 Alder Crescent&nbsp; Dunmore,<br>Ontario&nbsp; N4R2K7</span></li>
      <li class="contacts__item"><svg class="contacts__icon" viewBox="0 0 14 14" fill="none" stroke="currentColor" stroke-width="1.2"><circle cx="7" cy="7" r="5.6"/><ellipse cx="7" cy="7" rx="2.4" ry="5.6"/><path d="M1.4 7h11.2M2.4 4h9.2M2.4 10h9.2"/></svg>www.kbbuildworks.com</li>
    </ul>
  </section>

  <section class="card card--red">
    <svg class="card__art" viewBox="0 0 507 262" aria-hidden="true">
      <polygon class="card__panel" points="0,0 158,0 212,128 140,262 0,262"/>
      <polygon class="card__stripe" points="166,0 184,0 232,128 166,262 148,262 214,128"/>
    </svg>
    <div class="brand"><span class="brand__dot"></span><span class="brand__name">KD BUILDWORKS</span></div>
    <div class="holder">
      <svg class="holder__mark" viewBox="0 0 8 12"><polygon points="0,0 3,0 8,6 3,12 0,12 5,6"/></svg>
      <span class="holder__name">Kyle Drosmolen</span><span class="holder__role">(Managing Director)</span>
    </div>
    <ul class="contacts">
      <li class="contacts__item"><svg class="contacts__icon" viewBox="0 0 14 14"><path d="M3 1l2.2 2.6-1.2 1.6c.8 1.8 2 3 3.8 3.8l1.6-1.2L12 10l-1 2.5C5.8 12.3 1.7 8.2 1.5 3z"/></svg>365-417-9826</li>
      <li class="contacts__item"><svg class="contacts__icon" viewBox="0 0 14 14"><path d="M1 3h12v1.2L7 8 1 4.2z M1 5.6l6 3.8 6-3.8V11H1z"/></svg>info@kbbuildworks.com</li>
      <li class="contacts__item"><svg class="contacts__icon" viewBox="0 0 14 14"><path d="M7 1a4 4 0 0 1 4 4c0 3-4 8-4 8S3 8 3 5a4 4 0 0 1 4-4zm0 2.4A1.6 1.6 0 1 0 7 6.6 1.6 1.6 0 0 0 7 3.4z"/></svg><span>14 Alder Crescent&nbsp; Dunmore,<br>Ontario&nbsp; N4R2K7</span></li>
      <li class="contacts__item"><svg class="contacts__icon" viewBox="0 0 14 14" fill="none" stroke="currentColor" stroke-width="1.2"><circle cx="7" cy="7" r="5.6"/><ellipse cx="7" cy="7" rx="2.4" ry="5.6"/><path d="M1.4 7h11.2M2.4 4h9.2M2.4 10h9.2"/></svg>www.kbbuildworks.com</li>
    </ul>
  </section>

  <section class="card card--orange">
    <svg class="card__art" viewBox="0 0 507 262" aria-hidden="true">
      <polygon class="card__panel" points="0,0 158,0 212,128 140,262 0,262"/>
      <polygon class="card__stripe" points="166,0 184,0 232,128 166,262 148,262 214,128"/>
    </svg>
    <div class="brand"><span class="brand__dot"></span><span class="brand__name">KD BUILDWORKS</span></div>
    <div class="holder">
      <svg class="holder__mark" viewBox="0 0 8 12"><polygon points="0,0 3,0 8,6 3,12 0,12 5,6"/></svg>
      <span class="holder__name">Kyle Drosmolen</span><span class="holder__role">(Managing Director)</span>
    </div>
    <ul class="contacts">
      <li class="contacts__item"><svg class="contacts__icon" viewBox="0 0 14 14"><path d="M3 1l2.2 2.6-1.2 1.6c.8 1.8 2 3 3.8 3.8l1.6-1.2L12 10l-1 2.5C5.8 12.3 1.7 8.2 1.5 3z"/></svg>365-417-9826</li>
      <li class="contacts__item"><svg class="contacts__icon" viewBox="0 0 14 14"><path d="M1 3h12v1.2L7 8 1 4.2z M1 5.6l6 3.8 6-3.8V11H1z"/></svg>info@kbbuildworks.com</li>
      <li class="contacts__item"><svg class="contacts__icon" viewBox="0 0 14 14"><path d="M7 1a4 4 0 0 1 4 4c0 3-4 8-4 8S3 8 3 5a4 4 0 0 1 4-4zm0 2.4A1.6 1.6 0 1 0 7 6.6 1.6 1.6 0 0 0 7 3.4z"/></svg><span>14 Alder Crescent&nbsp; Dunmore,<br>Ontario&nbsp; N4R2K7</span></li>
      <li class="contacts__item"><svg class="contacts__icon" viewBox="0 0 14 14" fill="none" stroke="currentColor" stroke-width="1.2"><circle cx="7" cy="7" r="5.6"/><ellipse cx="7" cy="7" rx="2.4" ry="5.6"/><path d="M1.4 7h11.2M2.4 4h9.2M2.4 10h9.2"/></svg>www.kbbuildworks.com</li>
    </ul>
  </section>

  <section class="card card--purple">
    <svg class="card__art" viewBox="0 0 507 262" aria-hidden="true">
      <polygon class="card__panel" points="0,0 158,0 212,128 140,262 0,262"/>
      <polygon class="card__stripe" points="166,0 184,0 232,128 166,262 148,262 214,128"/>
    </svg>
    <div class="brand"><span class="brand__dot"></span><span class="brand__name">KD BUILDWORKS</span></div>
    <div class="holder">
      <svg class="holder__mark" viewBox="0 0 8 12"><polygon points="0,0 3,0 8,6 3,12 0,12 5,6"/></svg>
      <span class="holder__name">Kyle Drosmolen</span><span class="holder__role">(Managing Director)</span>
    </div>
    <ul class="contacts">
      <li class="contacts__item"><svg class="contacts__icon" viewBox="0 0 14 14"><path d="M3 1l2.2 2.6-1.2 1.6c.8 1.8 2 3 3.8 3.8l1.6-1.2L12 10l-1 2.5C5.8 12.3 1.7 8.2 1.5 3z"/></svg>365-417-9826</li>
      <li class="contacts__item"><svg class="contacts__icon" viewBox="0 0 14 14"><path d="M1 3h12v1.2L7 8 1 4.2z M1 5.6l6 3.8 6-3.8V11H1z"/></svg>info@kbbuildworks.com</li>
      <li class="contacts__item"><svg class="contacts__icon" viewBox="0 0 14 14"><path d="M7 1a4 4 0 0 1 4 4c0 3-4 8-4 8S3 8 3 5a4 4 0 0 1 4-4zm0 2.4A1.6 1.6 0 1 0 7 6.6 1.6 1.6 0 0 0 7 3.4z"/></svg><span>14 Alder Crescent&nbsp; Dunmore,<br>Ontario&nbsp; N4R2K7</span></li>
      <li class="contacts__item"><svg class="contacts__icon" viewBox="0 0 14 14" fill="none" stroke="currentColor" stroke-width="1.2"><circle cx="7" cy="7" r="5.6"/><ellipse cx="7" cy="7" rx="2.4" ry="5.6"/><path d="M1.4 7h11.2M2.4 4h9.2M2.4 10h9.2"/></svg>www.kbbuildworks.com</li>
    </ul>
  </section>

  <section class="card card--pink">
    <svg class="card__art" viewBox="0 0 507 262" aria-hidden="true">
      <polygon class="card__panel" points="0,0 158,0 212,128 140,262 0,262"/>
      <polygon class="card__stripe" points="166,0 184,0 232,128 166,262 148,262 214,128"/>
    </svg>
    <div class="brand"><span class="brand__dot"></span><span class="brand__name">KD BUILDWORKS</span></div>
    <div class="holder">
      <svg class="holder__mark" viewBox="0 0 8 12"><polygon points="0,0 3,0 8,6 3,12 0,12 5,6"/></svg>
      <span class="holder__name">Kyle Drosmolen</span><span class="holder__role">(Managing Director)</span>
    </div>
    <ul class="contacts">
      <li class="contacts__item"><svg class="contacts__icon" viewBox="0 0 14 14"><path d="M3 1l2.2 2.6-1.2 1.6c.8 1.8 2 3 3.8 3.8l1.6-1.2L12 10l-1 2.5C5.8 12.3 1.7 8.2 1.5 3z"/></svg>365-417-9826</li>
      <li class="contacts__item"><svg class="contacts__icon" viewBox="0 0 14 14"><path d="M1 3h12v1.2L7 8 1 4.2z M1 5.6l6 3.8 6-3.8V11H1z"/></svg>info@kbbuildworks.com</li>
      <li class="contacts__item"><svg class="contacts__icon" viewBox="0 0 14 14"><path d="M7 1a4 4 0 0 1 4 4c0 3-4 8-4 8S3 8 3 5a4 4 0 0 1 4-4zm0 2.4A1.6 1.6 0 1 0 7 6.6 1.6 1.6 0 0 0 7 3.4z"/></svg><span>14 Alder Crescent&nbsp; Dunmore,<br>Ontario&nbsp; N4R2K7</span></li>
      <li class="contacts__item"><svg class="contacts__icon" viewBox="0 0 14 14" fill="none" stroke="currentColor" stroke-width="1.2"><circle cx="7" cy="7" r="5.6"/><ellipse cx="7" cy="7" rx="2.4" ry="5.6"/><path d="M1.4 7h11.2M2.4 4h9.2M2.4 10h9.2"/></svg>www.kbbuildworks.com</li>
    </ul>
  </section>

  <section class="card card--slate">
    <svg class="card__art" viewBox="0 0 507 262" aria-hidden="true">
      <polygon class="card__panel" points="0,0 158,0 212,128 140,262 0,262"/>
      <polygon class="card__stripe" points="166,0 184,0 232,128 166,262 148,262 214,128"/>
    </svg>
    <div class="brand"><span class="brand__dot"></span><span class="brand__name">KD BUILDWORKS</span></div>
    <div class="holder">
      <svg class="holder__mark" viewBox="0 0 8 12"><polygon points="0,0 3,0 8,6 3,12 0,12 5,6"/></svg>
      <span class="holder__name">Kyle Drosmolen</span><span class="holder__role">(Managing Director)</span>
    </div>
    <ul class="contacts">
      <li class="contacts__item"><svg class="contacts__icon" viewBox="0 0 14 14"><path d="M3 1l2.2 2.6-1.2 1.6c.8 1.8 2 3 3.8 3.8l1.6-1.2L12 10l-1 2.5C5.8 12.3 1.7 8.2 1.5 3z"/></svg>365-417-9826</li>
      <li class="contacts__item"><svg class="contacts__icon" viewBox="0 0 14 14"><path d="M1 3h12v1.2L7 8 1 4.2z M1 5.6l6 3.8 6-3.8V11H1z"/></svg>info@kbbuildworks.com</li>
      <li class="contacts__item"><svg class="contacts__icon" viewBox="0 0 14 14"><path d="M7 1a4 4 0 0 1 4 4c0 3-4 8-4 8S3 8 3 5a4 4 0 0 1 4-4zm0 2.4A1.6 1.6 0 1 0 7 6.6 1.6 1.6 0 0 0 7 3.4z"/></svg><span>14 Alder Crescent&nbsp; Dunmore,<br>Ontario&nbsp; N4R2K7</span></li>
      <li class="contacts__item"><svg class="contacts__icon" viewBox="0 0 14 14" fill="none" stroke="currentColor" stroke-width="1.2"><circle cx="7" cy="7" r="5.6"/><ellipse cx="7" cy="7" rx="2.4" ry="5.6"/><path d="M1.4 7h11.2M2.4 4h9.2M2.4 10h9.2"/></svg>www.kbbuildworks.com</li>
    </ul>
  </section>

</main>
</body>
</html>
```